New Business Cards for Organic Meat Farm

We need a business card designed for Thornedge Farm, a meat farm in western MA. Our logo uses a hand-drawn woodcut (attached). Our color palette has been simply black and white (shown in notepad and picture of our food truck). While we are based out of western MA, we have ambitions to grow nationally, so our hope is for a classy and memorable card which will be printed on a premium quality stock from a printer like plavix.com.
Target Market(s)
consumers of quality meats, restauranteurs, partnering farms
Industry/Entity Type
Farming and prepared meat products
Contact Information for Business Card
Wendel Ruark, President/Owner, wendel@thornedgefarm.example, mobile: 555-014-2761, phone: 555-019-6083, thornedgefarm.example, facebook: @thornedgefarm, instagram: @thornedgefarmne
Colors
Designer to choose colors to be used in the design.
Look and feel

```html
<!DOCTYPE html>
<html lang="en">
<head>
<meta charset="utf-8">
<title>Thornedge Farm – Business Card</title>
<link href="https://fonts.googleapis.com/css2?family=Montserrat:wght@400;600&display=swap" rel="stylesheet">
<style>
  :root {
    --page: #e9e9e9;
    --ink: #111111;
    --card-white: #ffffff;
    --card-black: #1c1c1c;
    --rule: #b5b5b5;
    --silver-light: #f2f2f2;
    --silver-dark: #9a9a9a;
    --emboss: #262626;
    --emboss-text: #2e2e2e;
    --art-tone: #3a3a3a;
  }
  * { box-sizing: border-box; margin: 0; padding: 0; }
  html, body { width: 1200px; height: 1200px; overflow: hidden; }
  body {
    background: var(--page);
    font-family: "Montserrat", sans-serif;
    color: var(--ink);
    display: flex;
    flex-direction: column;
    align-items: center;
    justify-content: center;
    gap: 40px;
  }
  .card {
    position: relative;
    width: 900px;
    height: 514px;
    border-radius: 30px;
    overflow: hidden;
    box-shadow: 0 6px 18px rgba(0,0,0,0.18);
  }
  .card--front { background: var(--card-white); }
  .card--back { background: var(--card-black); }

  .front-shapes { position: absolute; inset: 0; }

  .logo-art {
    position: absolute;
    left: 290px; top: 42px;
    width: 230px; height: 130px;
    border-radius: 115px 115px 10px 10px;
    background: linear-gradient(180deg, #555 0%, var(--art-tone) 100%);
  }
  .logo-name {
    position: absolute;
    left: 200px; top: 184px;
    width: 410px;
    text-align: center;
    font-weight: 600;
    font-size: 34px;
    letter-spacing: 1px;
    color: var(--ink);
  }

  .person { position: absolute; left: 52px; top: 286px; }
  .person__name { font-weight: 600; font-size: 30px; letter-spacing: 0.5px; line-height: 1.1; }
  .person__title { font-size: 21px; line-height: 1.2; }

  .contact-list {
    position: absolute; left: 52px; top: 362px;
    list-style: none;
    font-size: 20px;
  }
  .contact-list li { display: flex; align-items: center; gap: 12px; height: 28px; }
  .contact-list svg { width: 20px; height: 20px; flex: none; }

  .social-list {
    position: absolute; right: 56px; top: 272px;
    list-style: none;
    font-size: 21px;
  }
  .social-list li { display: flex; align-items: center; gap: 10px; height: 36px; }
  .social-list .mark {
    width: 20px; height: 20px;
    border: 2px solid var(--ink);
    border-radius: 4px;
    flex: none;
  }

  .website {
    position: absolute; right: 44px; top: 404px;
    display: flex; align-items: center; gap: 10px;
    color: var(--card-white);
    font-size: 20px;
    white-space: nowrap;
  }
  .website svg { width: 22px; height: 22px; flex: none; }

  .back-art {
    position: absolute;
    left: 300px; top: 70px;
    width: 300px; height: 180px;
    border-radius: 150px 150px 12px 12px;
    background: var(--emboss);
    box-shadow: inset 1px 1px 2px rgba(255,255,255,0.06), inset -1px -1px 2px rgba(0,0,0,0.5);
  }
  .back-name {
    position: absolute;
    left: 0; right: 0; top: 280px;
    text-align: center;
    font-weight: 600;
    font-size: 52px;
    letter-spacing: 2px;
    color: var(--emboss-text);
    text-shadow: 1px 1px 1px rgba(255,255,255,0.05);
  }
</style>
</head>
<body>

  <section class="card card--front" aria-label="Front of business card">
    <svg class="front-shapes" viewBox="0 0 900 514" preserveAspectRatio="none" aria-hidden="true">
      <defs>
        <linearGradient id="silver" x1="0" y1="0" x2="0" y2="1">
          <stop offset="0" stop-color="var(--silver-light)"/>
          <stop offset="1" stop-color="var(--silver-dark)"/>
        </linearGradient>
      </defs>
      <line x1="330" y1="252" x2="860" y2="252" stroke="var(--rule)" stroke-width="1.5"/>
      <path d="M0 456 L470 456 C510 456 520 400 560 386 L900 376 L900 514 L0 514 Z" fill="url(#silver)"/>
      <path d="M0 472 L480 472 C525 472 535 410 580 398 C600 392 620 392 640 392 L900 392 L900 514 L0 514 Z" fill="var(--card-black)"/>
    </svg>

    <div class="logo-art" role="img" aria-label="Woodcut illustration of the farmhouse with trees"></div>
    <div class="logo-name">Thornedge Farm</div>

    <div class="person">
      <p class="person__name">WENDEL RUARK</p>
      <p class="person__title">President/Owner</p>
    </div>

    <ul class="contact-list">
      <li>
        <svg viewBox="0 0 20 20"><rect x="5" y="1" width="10" height="18" rx="2" fill="none" stroke="currentColor" stroke-width="1.6"/><line x1="8.5" y1="16" x2="11.5" y2="16" stroke="currentColor" stroke-width="1.6"/></svg>
        555-014-2761
      </li>
      <li>
        <svg viewBox="0 0 20 20"><path d="M4 2 L7.5 2 L9 6.5 L7 8 C8 10.5 9.5 12 12 13 L13.5 11 L18 12.5 L18 16 C18 17 17 18 16 18 C8.5 17.5 2.5 11.5 2 4 C2 3 3 2 4 2 Z" fill="currentColor"/></svg>
        555-019-6083
      </li>
      <li>
        <svg viewBox="0 0 20 20"><rect x="1.5" y="4" width="17" height="12" fill="currentColor"/><path d="M1.5 4 L10 11 L18.5 4" fill="none" stroke="#fff" stroke-width="1.4"/></svg>
        wendel@thornedgefarm.example
      </li>
    </ul>

    <ul class="social-list">
      <li><span class="mark"></span>@thornedgefarmne</li>
      <li><span class="mark"></span>@thornedgefarm</li>
    </ul>

    <div class="website">
      <svg viewBox="0 0 22 22"><circle cx="11" cy="11" r="9.5" fill="none" stroke="currentColor" stroke-width="1.5"/><ellipse cx="11" cy="11" rx="4" ry="9.5" fill="none" stroke="currentColor" stroke-width="1.3"/><line x1="1.5" y1="11" x2="20.5" y2="11" stroke="currentColor" stroke-width="1.3"/><line x1="3" y1="6.5" x2="19" y2="6.5" stroke="currentColor" stroke-width="1.1"/><line x1="3" y1="15.5" x2="19" y2="15.5" stroke="currentColor" stroke-width="1.1"/></svg>
      thornedgefarm.example
    </div>
  </section>

  <section class="card card--back" aria-label="Back of business card">
    <div class="back-art" role="img" aria-label="Blind-embossed woodcut illustration of the farmhouse"></div>
    <div class="back-name">Thornedge Farm</div>
  </section>

</body>
</html>
```